Corvale Holdings Business Cards

Hello. I need business cards designed with our new logo. I'd like to see at least 3 different designs. At least one with a dark background, and at least one with a white background. Maybe one with gray or blue for the background. Play with gradient colors and maybe even insert a pic of a skyline in the background of one or more of them. Use your judgement. We will need 2 cards printed. They need to accommodate the employee name, title, company address, phone, email, and website. Thanks.

Target Market(s)

Wealthy mature investors.

Contact Information for Business Card

Single-sided, professional, clean design that incorporates our logo.

Font styles to use
Sans Serif

Requirements
Must have
• Our new logo needs to be featured on it. (See attached.)
• Employee Name (In all CAPS)
• Title
• Street Address, City, ST Zip Code
• Cell Phone #, Email Address, Website Address
Nice to have
• Design that blends well with our new logo and its colors, or a city scape or other graphic design that looks like an apartment complex in the background. Blues and grays are nice, but use your judgement.
Should not have
• Modern or oriental looking designs or bright colors.

```html
<!DOCTYPE html>
<html lang="en">
<head>
<meta charset="utf-8">
<title>Corvale Holdings Business Cards</title>
<link href="https://fonts.googleapis.com/css2?family=Montserrat:wght@600;700&family=Arimo:wght@400;700&display=swap" rel="stylesheet">
<style>
  :root {
    --brand-blue: #29a6e0;
    --ink-gray: #4a4a4d;
    --paper: #ffffff;
    --backdrop: #e9ebee;
    --photo-light: #d9d9d9;
    --photo-dark: #6e6e6e;
  }
  * { margin: 0; padding: 0; box-sizing: border-box; }
  html, body { width: 1200px; height: 800px; overflow: hidden; }
  body { background: var(--backdrop); font-family: "Arimo", Arial, sans-serif; position: relative; }

  .card {
    position: absolute; left: 320px; width: 560px; height: 320px;
    border-radius: 22px; overflow: hidden;
    box-shadow: 0 8px 24px rgba(0,0,0,.15);
  }
  .card--front { top: 50px; background: var(--brand-blue); color: var(--paper); }
  .card--back { top: 430px; background: var(--paper); }

  /* Front */
  .front-brand { position: absolute; left: 0; right: 0; top: 112px; text-align: center; }
  .front-brand__name {
    font-family: "Montserrat", sans-serif; font-weight: 700;
    font-size: 40px; letter-spacing: 2px; line-height: 1;
  }
  .front-brand__sub {
    font-family: "Montserrat", sans-serif; font-weight: 700;
    font-size: 40px; letter-spacing: 2px; line-height: 1.1;
  }
  .front-web {
    position: absolute; left: 0; right: 0; top: 230px; text-align: center;
    font-size: 14px; letter-spacing: 3px; font-weight: 700;
  }

  /* Back */
  .back-art { position: absolute; inset: 0; }
  .back-brand { position: absolute; left: 30px; top: 34px; display: flex; align-items: center; gap: 12px; }
  .back-brand__mark { width: 18px; height: 18px; background: var(--brand-blue); }
  .back-brand__name {
    font-family: "Montserrat", sans-serif; font-weight: 700;
    font-size: 26px; letter-spacing: 1px; color: var(--brand-blue); line-height: 1.05;
  }
  .contact { position: absolute; left: 30px; top: 172px; color: var(--paper); font-size: 11.5px; line-height: 1.35; }
  .contact__name { font-family: "Montserrat", sans-serif; font-weight: 700; font-size: 17px; letter-spacing: .5px; line-height: 1.1; }
  .contact__title { font-size: 13px; margin-bottom: 6px; }
  .contact__row { display: flex; align-items: center; gap: 8px; margin-top: 3px; }
  .contact__icon { width: 14px; height: 14px; flex: none; }
  .back-web {
    position: absolute; right: 28px; top: 240px;
    font-size: 14px; letter-spacing: 1px; color: var(--ink-gray);
  }
  .back-web__domain { color: var(--brand-blue); }
</style>
</head>
<body>

  <section class="card card--front" aria-label="Card front">
    <div class="front-brand">
      <div class="front-brand__name">CORVALE</div>
      <div class="front-brand__sub">HOLDINGS</div>
    </div>
    <div class="front-web">WWW.CORVALEHOLDINGS.COM</div>
  </section>

  <section class="card card--back" aria-label="Card back">
    <svg class="back-art" width="560" height="320" viewBox="0 0 560 320">
      <defs>
        <linearGradient id="skylineTone" x1="0" y1="0" x2="1" y2="1">
          <stop offset="0" stop-color="var(--photo-light)"/>
          <stop offset="1" stop-color="var(--photo-dark)"/>
        </linearGradient>
      </defs>
      <path d="M290 0 L560 0 L560 210 L330 210 Z" fill="url(#skylineTone)"
            role="img" aria-label="Black and white aerial photograph of a city skyline with tall buildings"/>
      <path d="M0 160 L330 112 Q356 108 352 132 L300 320 L0 320 Z" fill="var(--brand-blue)"/>
    </svg>

    <div class="back-brand">
      <span class="back-brand__mark"></span>
      <div class="back-brand__name">CORVALE<br>HOLDINGS</div>
    </div>

    <div class="contact">
      <div class="contact__name">ELIAS MARWOOD</div>
      <div class="contact__title">Founder</div>
      <div>PO BOX 418, Alder Street,</div>
      <div>Suite 2, Phoenix, AZ 85004</div>
      <div class="contact__row">
        <svg class="contact__icon" viewBox="0 0 14 14"><rect x="3" y="1" width="8" height="12" rx="1.5" fill="none" stroke="#fff" stroke-width="1.4"/><circle cx="7" cy="11" r=".8" fill="#fff"/></svg>
        <span>555.014.2290</span>
      </div>
      <div class="contact__row">
        <svg class="contact__icon" viewBox="0 0 14 14"><rect x="1" y="3" width="12" height="8" rx="1" fill="none" stroke="#fff" stroke-width="1.4"/><path d="M1.5 3.5 L7 8 L12.5 3.5" fill="none" stroke="#fff" stroke-width="1.4"/></svg>
        <span>info@corvaleholdings.com</span>
      </div>
    </div>

    <div class="back-web">www.<span class="back-web__domain">CORVALEHOLDINGS</span>.com</div>
  </section>

</body>
</html>
```